Zielgruppe
Ich suche ein ansprechendes Cover-Design für mein E-Book. Es handelt sich um einen Ratgeber über Selbstliebe und meine Zielgruppe sind Frauen im Alter zwischen 18 und 40 Jahren.
Aufgabenstellung
Klare Designs, die das Thema des Ratgebers unterstreichen und nicht durch unnötige Details und unlesbare Verschnörkelungen ablenken. Die weibliche Zielgruppe sollte vor allem angesprochen werden, dies sollte auch in der Farbauswahl berücksichtigt werden. Das bedeutet helle Farbtöne wie rosa, rot, hellblau oder pastellgelb.
Die Umsetzung des Motivs überlasse ich der Kreativität des Designers. Es können sowohl Stockfotos von einer jungen Frau gewählt werden, die Freude ausstrahlt und sich wohl in ihrer Haut fühlt (wo vielleicht auch warmes Licht oder Sonnenschein auf dem Cover zu sehen sind) oder ein rein graphisches Bild aus zusammengesetzten Elementen, die eine junge Frau zeigen und ihre Beziehung zur Selbstliebe deutlich wird. Es muss nicht zwangsläufig ein Herz abgebildet werden, nur weil es das erste ist, was man vielleicht mit Liebe assoziiert, auch wenn ein kreativer Umgang mit dem Herz als Symbol eine durchaus ansprechende Wirkung haben kann. Wichtig wäre mir eine kreative Umsetzung im Bild, wodurch das Thema der 'Selbstliebe' sofort deutlich wird und den Käufer anspricht. Der Titel sollte genauso deutlich hervorstechen wie das zentrale Motiv. Außerdem sollte gleich erkennbar sein, dass es sich nicht um einen Roman, sondern um einen Ratgeber handelt. Daher bin ich an einer graphischen Aufbereitung genauso wie an einem Fotomotiv interessiert. Bereits existierende Cover zu einem ähnlichen Ratgeber- Thema, die ich ansprechend finde, füge ich im Anhang hinzu.
Bitte nicht die im Anhang eingefügten Dateien verwenden, da sie urheberrechtlich geschützt sind! Sie dienen nur als Interpretationsvorschlag.
Titel: Gelassen atmen
Untertitel: Wie du Gewohnheiten änderst und mehr Klarheit im täglichen Alltag gewinnst
Autorenname: Jora Wendt
Der Buchrücken soll farblich an das Cover angepasst werden. Der Buchrückentext folgt noch im Anhang.
Das E-Book wird es auch als Paperback Buch geben. Der Umfang des Ra..

```html
<!DOCTYPE html>
<html lang="de">
<head>
<meta charset="utf-8">
<title>Gelassen atmen – Buchumschlag</title>
<link rel="stylesheet" href="https://fonts.googleapis.com/css2?family=Oswald:wght@400;500&family=Didact+Gothic&family=Allura&display=swap">
<style>
  :root {
    --orange: #f39a3e;
    --orange-box: rgba(244, 150, 56, 0.9);
    --orange-title: #f2a35a;
    --brown: #6a3812;
    --white: #ffffff;
    --sky-top: #c9beb4;
    --sky-mid: #f4f1ec;
    --sun: #f6b24a;
    --field: #c46a22;
    --field-dark: #6e4628;
  }
  * { margin: 0; padding: 0; box-sizing: border-box; }
  html, body { width: 1200px; height: 843px; overflow: hidden; background: #fff; }
  .cover {
    position: relative; width: 1200px; height: 843px; overflow: hidden;
    font-family: "Didact Gothic", "Century Gothic", sans-serif;
  }
  .cover-photo { position: absolute; inset: 0; width: 1200px; height: 843px; }

  /* back cover */
  .blurb-box {
    position: absolute; left: 102px; top: 99px; width: 343px; height: 627px;
    background: var(--orange-box);
  }
  .author-photo { position: absolute; left: 52px; top: 74px; width: 165px; height: 175px; z-index: 2; }
  .back-subtitle {
    position: absolute; left: 231px; top: 189px; width: 195px;
    color: var(--white); font-size: 15px; line-height: 18.5px;
  }
  .blurb {
    position: absolute; left: 138px; top: 297px; width: 276px;
    color: var(--white); font-size: 14.6px; line-height: 18.4px;
    text-align: justify; hyphens: auto;
  }
  .signature {
    position: absolute; right: 776px; top: 570px;
    color: var(--white); font-family: "Allura", cursive; font-size: 27px; white-space: nowrap;
  }

  /* spine */
  .spine { position: absolute; left: 554px; top: 0; width: 89px; height: 843px; background: var(--orange); }
  .spine-title, .spine-subtitle { position: absolute; writing-mode: vertical-rl; transform: rotate(180deg); white-space: nowrap; color: var(--white); }
  .spine-title {
    left: 572px; bottom: 84px;
    font-family: "Oswald", sans-serif; font-weight: 500; font-size: 48px; line-height: 52px;
  }
  .spine-subtitle { left: 580px; bottom: 435px; font-size: 15.5px; line-height: 22px; }
  .spine-author {
    position: absolute; left: 577px; top: 788px;
    color: var(--white); font-size: 22px; line-height: 21px;
  }

  /* front cover */
  .front-photo { position: absolute; left: 690px; top: 160px; width: 400px; height: 683px; }
  .front-title {
    position: absolute; right: 28px; top: 16px;
    font-family: "Oswald", sans-serif; font-weight: 400; font-size: 72px; letter-spacing: 2px;
    color: var(--orange-title); white-space: nowrap;
  }
  .front-subtitle {
    position: absolute; right: 22px; top: 110px; text-align: right;
    color: var(--brown); font-size: 16px; line-height: 21px; white-space: nowrap;
  }
  .front-author {
    position: absolute; right: 27px; top: 783px;
    color: var(--orange-title); font-size: 24px; white-space: nowrap;
  }
  .series-number {
    position: absolute; left: 1178px; top: 817px;
    color: var(--white); font-size: 20px; font-weight: bold; white-space: nowrap;
  }
</style>
</head>
<body>
<main class="cover">
  <svg class="cover-photo" viewBox="0 0 1200 843" role="img" aria-label="Foto: Feld mit hohem Gras bei Sonnenuntergang">
    <defs>
      <linearGradient id="sky" x1="0" y1="0" x2="0" y2="1">
        <stop offset="0" stop-color="var(--sky-top)"/>
        <stop offset="0.35" stop-color="var(--sky-mid)"/>
        <stop offset="0.62" stop-color="#f7e2c4"/>
        <stop offset="0.74" stop-color="var(--sun)"/>
        <stop offset="0.86" stop-color="var(--field)"/>
        <stop offset="1" stop-color="var(--field-dark)"/>
      </linearGradient>
    </defs>
    <rect width="1200" height="843" fill="url(#sky)"/>
  </svg>

  <section class="back-cover">
    <div class="blurb-box"></div>
    <svg class="author-photo" viewBox="0 0 165 175" role="img" aria-label="Porträtfoto der Autorin">
      <defs>
        <linearGradient id="portrait" x1="0" y1="0" x2="1" y2="1">
          <stop offset="0" stop-color="#e4ebf4"/>
          <stop offset="1" stop-color="#c9d3e0"/>
        </linearGradient>
      </defs>
      <rect width="165" height="175" fill="url(#portrait)"/>
    </svg>
    <p class="back-subtitle">Wie du Gewohnheiten änderst und mehr Klarheit im täglichen Alltag gewinnst</p>
    <p class="blurb" lang="de">Lorem ipsum dolor sit amet, consetetur sadipscing elitr, sed diam nonumy eirmod tempor invidunt ut labore et dolore magna aliquyam erat, sed diam voluptua. At vero eos et accusam et justo duo dolores et ea rebum. Stet clita kasd gubergren, no sea takimata sanctus est Lorem ipsum dolor sit amet. Lorem ipsum dolor sit amet, consetetur sadipscing elitr, sed diam nonumy eirmod tempor invidunt ut labore et dolore magna aliquyam erat, sed diam voluptua. At vero eos et accusam et justo duo dolores et ea rebum. Stet clita kasd gubergren, no sea takimata sanctus est Lorem ipsum dolor sit amet.</p>
    <p class="signature">Jora Wendt</p>
  </section>

  <section class="spine-area">
    <div class="spine"></div>
    <p class="spine-subtitle">Wie du Gewohnheiten änderst<br>und mehr Klarheit im täglichen Alltag gewinnst</p>
    <h2 class="spine-title">Gelassen atmen</h2>
    <p class="spine-author">Jora<br>Wendt</p>
  </section>

  <section class="front-cover">
    <svg class="front-photo" viewBox="0 0 400 683" role="img" aria-label="Foto: junge Frau mit lockigem Haar umarmt sich selbst im Gegenlicht">
      <defs>
        <linearGradient id="motif" x1="0" y1="0" x2="0" y2="1">
          <stop offset="0" stop-color="#5a3a26"/>
          <stop offset="0.3" stop-color="#b7876a"/>
          <stop offset="0.6" stop-color="#8f8a96"/>
          <stop offset="0.85" stop-color="#c07a4a"/>
          <stop offset="1" stop-color="#2e231e"/>
        </linearGradient>
      </defs>
      <path d="M40 683 L40 200 Q40 0 200 0 Q360 0 360 200 L360 683 Z" fill="url(#motif)" opacity="0.85"/>
    </svg>
    <h1 class="front-title">Gelassen atmen</h1>
    <p class="front-subtitle">Wie du Gewohnheiten änderst<br>und mehr Klarheit im täglichen Alltag gewinnst</p>
    <p class="front-author">Jora Wendt</p>
    <p class="series-number">#3</p>
  </section>
</main>
</body>
</html>
```